GUARANTEED! Simple website for independent event planner and consultant...

I need a website that is no more than 5 or 6 pages to illustrate who I am and what I can offer to groups who book hotels for meetings and conferences. I have 20 years of experience planning meetings within hotels and I am now ready to go out on my own and help clients choose venues, negotiate contracts and plan effective meetings. I will focus on clients planning meetings in the mountains of Colorado but I am willing to travel as well. I want to work with a person who is collaborative and can direct me on what they need to move the project along quickly. I already have my logo, a hosting site and work e-mail address. Also, I recently hired a photographer to do head shots. Lastly, it important for me to be able to talk on the phone or skype with this person, as needed and I must be able to make changes to my site down the road when necessary...

Target Market(s)

Corporate Groups

Industry/Entity Type

Event Planning

Coding

Coded - Design and coding required

Number of Pages Required

5+ page

Font styles to use
Sans Serif

Requirements
Must have
• About me page, event planning services offered page, task force and consulting work page, testimonials page, page for blogs, page to contact me/request a proposal. May need advice on what else I need...
Nice to have
• I want it to look sharp and professional. I want people to look at my site and know immediately that they can trust me and the work I can do.
• I don't want it to look like it is over the top as I am not a HUGE company but I do want it to be professional and easy to view and navigate.
Should not have
• Bright colors
• My logo is bright orange and black. I have also used dark grey and orange. See below:
• Orange:
• C = 0
• M = 64
• Y = 100
• K = 0
• Gray:
• C = 67
• M = 60
• Y = 59
• K = 45
• Font: Gotham Book and Gotham Bold

```html
<!DOCTYPE html>
<html lang="en">
<head>
<meta charset="utf-8">
<title>Laura Benning CMP, CMM — Event Planner &amp; Consultant</title>
<link rel="stylesheet" href="https://fonts.googleapis.com/css2?family=Montserrat:wght@400;500&display=swap">
<style>
  :root {
    --orange: #f47b20;
    --charcoal: #424042;
    --ink: #3a3838;
    --cream: #f3eee7;
    --white: #ffffff;
    --veil: rgba(60, 60, 62, 0.72);
  }
  * { margin: 0; padding: 0; box-sizing: border-box; }
  html, body { width: 1200px; height: 2597px; overflow: hidden; }
  body {
    font-family: "Montserrat", sans-serif;
    color: var(--ink);
    background: var(--white);
    position: relative;
  }

  .hero {
    position: absolute; left: 0; top: 0; width: 1200px; height: 783px;
    background: linear-gradient(180deg, #a9c4b8 0%, #b8ccbd 28%, #8fa8a2 46%, #4e6a66 60%, #2f4a45 74%, #253a30 88%, #4a3c2e 100%);
  }
  .brand {
    display: flex; align-items: center; gap: 14px;
    color: var(--orange); font-weight: 500; font-size: 21px; line-height: 26px; letter-spacing: 1px;
    text-transform: uppercase;
  }
  .brand-square { width: 22px; height: 22px; background: var(--orange); flex: none; }
  .hero .brand { position: absolute; left: 62px; top: 70px; width: 270px; }
  .main-nav {
    position: absolute; top: 100px; left: 0; width: 1200px; height: 16px;
    font-size: 12px; letter-spacing: 0.3px; color: #2b2b2b; text-transform: uppercase;
  }
  .main-nav a { position: absolute; color: inherit; text-decoration: none; white-space: nowrap; }
  .hero-title, .hero-subtitle {
    position: absolute; background: var(--veil); color: var(--white);
    display: flex; align-items: center; justify-content: center;
    text-transform: uppercase; white-space: nowrap; font-weight: 400;
  }
  .hero-title { left: 294px; top: 370px; width: 613px; height: 91px; font-size: 38px; letter-spacing: 1px; }
  .hero-subtitle { left: 332px; top: 495px; width: 536px; height: 70px; font-size: 29px; letter-spacing: 0.8px; }

  .about {
    position: absolute; left: 0; top: 783px; width: 1200px; height: 642px;
    background: var(--cream);
  }
  .headshot {
    position: absolute; left: 152px; top: 110px; width: 283px; height: 423px;
    background: linear-gradient(160deg, #cfcfcf 0%, #8f8f8f 45%, #262626 100%);
  }
  .about-heading {
    position: absolute; left: 513px; top: 152px;
    font-weight: 400; font-size: 33px; letter-spacing: 1px; color: var(--ink);
  }
  .about-text {
    position: absolute; left: 518px; top: 206px; width: 535px;
    font-size: 21px; line-height: 25px; color: #4a4848;
  }
  .about-text strong { font-weight: 500; color: var(--ink); }

  .services {
    position: absolute; left: 0; top: 1425px; width: 1200px; height: 760px;
    background: var(--white);
  }
  .service-card {
    position: absolute; top: 83px; width: 296px; height: 485px;
    background: var(--cream); padding: 0 16px;
  }
  .service-card:nth-child(1) { left: 61px; }
  .service-card:nth-child(2) { left: 452px; }
  .service-card:nth-child(3) { left: 843px; }
  .service-title {
    height: 85px; display: flex; align-items: center; justify-content: center;
    font-weight: 400; font-size: 34px; letter-spacing: 1px; text-transform: uppercase; color: var(--ink);
  }
  .service-rule { height: 7px; background: var(--orange); }
  .service-text { margin-top: 20px; font-size: 21px; line-height: 25px; color: #4a4848; }

  .footer-band { position: absolute; left: 0; top: 2185px; width: 1200px; height: 40px; background: var(--orange); }
  .site-footer {
    position: absolute; left: 0; top: 2225px; width: 1200px; height: 372px;
    background: var(--charcoal);
  }
  .site-footer .brand { position: absolute; left: 0; width: 1200px; top: 160px; justify-content: center; }
</style>
</head>
<body>

<header class="hero" role="img" aria-label="Photograph of a snow-capped mountain peak above a forested valley under a pale cloudy sky">
  <div class="brand"><span class="brand-square"></span><span>Summit<br>Event Management</span></div>
  <nav class="main-nav">
    <a href="#about" style="left:384px">About Me</a>
    <a href="#planning" style="left:492px">Event Planning</a>
    <a href="#consulting" style="left:672px">Task Force and Consulting</a>
    <a href="#reviews" style="left:925px">Reviews</a>
    <a href="#contact" style="left:1032px">Contact Me</a>
  </nav>
  <h1 class="hero-title">Laura Benning CMP, CMM</h1>
  <p class="hero-subtitle">Event Planner &amp; Consultant</p>
</header>

<section class="about" id="about">
  <div class="headshot" role="img" aria-label="Black and white headshot portrait of the planner"></div>
  <h2 class="about-heading">#ABOUT</h2>
  <p class="about-text"><strong>Lorem Ipsum</strong> is simply dummy text of the printing and typesetting industry. Lorem Ipsum has been the industry's standard dummy text ever since the 1500s, when an unknown printer took a galley of type and scrambled it to make a type specimen book. It has survived not only five centuries, but also the leap into electronic typesetting, remaining essentially unchanged. It was popularised in the 1960s with the release of Letraset sheets containing Lorem Ipsum passages, and more recently with desktop publishing software like</p>
</section>

<section class="services" id="planning">
  <article class="service-card">
    <h3 class="service-title">Service 1</h3>
    <div class="service-rule"></div>
    <p class="service-text">when an unknown printer took a galley of type and scrambled it to make a type specimen book. It has survived not only five centuries, but also the leap into electronic typesetting, remaining essentially unchanged. It was popularised in the 1960s with the release of Letraset sheets containing Lorem Ipsum</p>
  </article>
  <article class="service-card">
    <h3 class="service-title">Service 2</h3>
    <div class="service-rule"></div>
    <p class="service-text">when an unknown printer took a galley of type and scrambled it to make a type specimen book. It has survived not only five centuries, but also the leap into electronic typesetting, remaining essentially unchanged. It was popularised in the 1960s with the release of Letraset sheets containing Lorem Ipsum</p>
  </article>
  <article class="service-card">
    <h3 class="service-title">Service 3</h3>
    <div class="service-rule"></div>
    <p class="service-text">when an unknown printer took a galley of type and scrambled it to make a type specimen book. It has survived not only five centuries, but also the leap into electronic typesetting, remaining essentially unchanged. It was popularised in the 1960s with the release of Letraset sheets containing Lorem Ipsum</p>
  </article>
</section>

<div class="footer-band"></div>
<footer class="site-footer" id="contact">
  <div class="brand"><span class="brand-square"></span><span>Summit<br>Event Management</span></div>
</footer>

</body>
</html>
```